Design for schnapps bottle label "Sol Terrado"

Hi! On a small land lot we are producing our own Italian schnapps "Grappa". For the bottles we would like to modernize our current labes that you find below. The two cats looking at each other should remain, but updated and more modern. I am very much looking forward to your suggestions. Best, Joel

Target Market(s)

Schnapps bottle label

Requirements
Must have
• Cats should resemble the cats that are decorating the house entry (see attached), however, should have a more modern appearance.

Text elements should remain: "Grappa", "Sol Terrado", "Legnoso", "[Vintage Year], "Raccolta No", "Vol %"
Should not have
• Current ornament can be used, replaced or deleted (whatever looks best)

```html
<!DOCTYPE html>
<html lang="it">
<head>
<meta charset="utf-8">
<title>Grappa Legnoso 2015 – Sol Terrado label</title>
<link rel="stylesheet" href="https://fonts.googleapis.com/css2?family=Della+Respira&family=Rochester&display=swap">
<style>
  :root {
    --page: #ffffff;
    --orange: #f48f23;
    --orange-light: #f8ab5a;
    --ink: #3f3a39;
    --cream: #ffffff;
    --cat-dark: #3b3a3d;
    --cat-mid: #5a585c;
    --ornament: #fde3c6;
  }
  html, body {
    margin: 0;
    padding: 0;
    width: 905px;
    height: 1200px;
    overflow: hidden;
    background: var(--page);
  }
  .canvas {
    position: relative;
    width: 905px;
    height: 1200px;
  }
  .label {
    position: absolute;
    left: 0;
    top: 0;
    width: 690px;
    height: 971px;
    transform-origin: 0 0;
    transform: translate(67px, 58px) scale(1.116);
    background: var(--orange);
    box-shadow: 0 2px 6px rgba(0,0,0,0.25);
    overflow: hidden;
  }
  .label__backdrop {
    position: absolute;
    inset: 0;
  }
  .ornament {
    position: absolute;
    background: var(--ornament);
    opacity: 0.55;
    border-radius: 40px;
  }
  .ornament--top { left: 68px; top: 16px; width: 555px; height: 100px; border-radius: 50px 50px 60px 60px; }
  .ornament--bottom { left: 45px; top: 918px; width: 595px; height: 28px; border-radius: 14px; }
  .ornament--side-top-left { left: 30px; top: 140px; width: 20px; height: 55px; }
  .ornament--side-mid-left { left: 22px; top: 410px; width: 36px; height: 190px; }
  .ornament--side-low-left { left: 30px; top: 812px; width: 20px; height: 60px; }
  .ornament--side-top-right { left: 635px; top: 140px; width: 20px; height: 55px; }
  .ornament--side-mid-right { left: 627px; top: 410px; width: 36px; height: 190px; }
  .ornament--side-low-right { left: 635px; top: 812px; width: 20px; height: 60px; }

  .cats {
    position: absolute;
    left: 80px;
    top: 585px;
    width: 530px;
    height: 100px;
    background: radial-gradient(ellipse at 30% 55%, var(--cat-mid), var(--cat-dark) 70%, transparent 72%),
                radial-gradient(ellipse at 70% 55%, var(--cat-mid), var(--cat-dark) 70%, transparent 72%);
    background-size: 50% 100%, 50% 100%;
    background-position: left center, right center;
    background-repeat: no-repeat;
  }

  .title {
    position: absolute;
    left: 0;
    width: 690px;
    top: 170px;
    margin: 0;
    text-align: center;
    font-family: "Della Respira", serif;
    font-weight: 400;
    font-size: 168px;
    line-height: 1;
    color: var(--ink);
    text-shadow: 1px 1px 0 var(--cream);
  }
  .vintage {
    position: absolute;
    left: 0;
    width: 690px;
    top: 400px;
    text-align: center;
    font-family: "Rochester", cursive;
    font-size: 68px;
    line-height: 1;
    color: var(--cream);
  }
  .vintage__year {
    font-family: "Della Respira", serif;
    font-size: 62px;
    margin-left: 18px;
  }
  .connector {
    position: absolute;
    left: 0;
    width: 690px;
    top: 510px;
    text-align: center;
    font-family: "Rochester", cursive;
    font-size: 40px;
    line-height: 1;
    color: var(--cream);
  }
  .producer {
    position: absolute;
    left: 0;
    width: 690px;
    top: 712px;
    text-align: center;
    font-family: "Rochester", cursive;
    font-size: 78px;
    line-height: 1;
    color: var(--cream);
  }
  .producer__initial { color: var(--ink); }
  .meta {
    position: absolute;
    top: 850px;
    font-family: "Rochester", cursive;
    font-size: 30px;
    line-height: 1;
    color: var(--ink);
  }
  .meta--batch { left: 105px; }
  .meta--abv { right: 105px; font-size: 24px; top: 855px; }
</style>
</head>
<body>
<div class="canvas">
  <div class="label">
    <svg class="label__backdrop" viewBox="0 0 690 971" width="690" height="971" aria-hidden="true">
      <path d="M690 0 L690 300 C 640 420 560 520 500 640 C 470 700 480 780 560 870 C 620 930 670 950 690 971 Z" fill="var(--orange-light)" opacity="0.8"/>
      <path d="M0 550 C 40 700 60 830 140 900 C 180 940 230 960 270 971 L0 971 Z" fill="var(--orange-light)" opacity="0.6"/>
      <path d="M520 110 C 640 130 700 260 620 420 C 560 540 480 620 490 740 C 500 840 600 900 690 960" fill="none" stroke="var(--cream)" stroke-opacity="0.55" stroke-width="3"/>
      <path d="M30 740 C 60 660 120 600 170 560" fill="none" stroke="var(--cream)" stroke-opacity="0.45" stroke-width="2"/>
      <line x1="40" y1="150" x2="40" y2="870" stroke="var(--cream)" stroke-width="1.5"/>
      <line x1="645" y1="150" x2="645" y2="870" stroke="var(--cream)" stroke-width="1.5"/>
    </svg>

    <div class="ornament ornament--top" role="img" aria-label="Curling flourish ornament with a small hanging drop at the centre"></div>
    <div class="ornament ornament--side-top-left" role="img" aria-label="Small drop ornament"></div>
    <div class="ornament ornament--side-mid-left" role="img" aria-label="Looping scroll ornament"></div>
    <div class="ornament ornament--side-low-left" role="img" aria-label="Small drop ornament"></div>
    <div class="ornament ornament--side-top-right" role="img" aria-label="Small drop ornament"></div>
    <div class="ornament ornament--side-mid-right" role="img" aria-label="Looping scroll ornament"></div>
    <div class="ornament ornament--side-low-right" role="img" aria-label="Small drop ornament"></div>
    <div class="ornament ornament--bottom" role="img" aria-label="Flourish line ornament with arrow ends"></div>

    <h1 class="title">Grappa</h1>
    <div class="vintage">“legnoso”<span class="vintage__year">2015</span></div>
    <div class="connector">di</div>

    <div class="cats" role="img" aria-label="Two stylised dark grey cats with white tail tips, crouching and facing each other"></div>

    <div class="producer"><span class="producer__initial">S</span>ol <span class="producer__initial">T</span>errado</div>

    <div class="meta meta--batch">Raccolta No. 01</div>
    <div class="meta meta--abv">41.0% Vol.</div>
  </div>
</div>
</body>
</html>
```